Empresa de Asesoramiento en inversiones necesita un nuevo diseño de web

Necesitamos un nuevo diseño de pagina web que nos permita impulsar el posicionamiento de marca en los clientes.
Somos una empresa Española que busca, coordina y gestiona las alternativas de inversión que mejor se ajustan a las necesidades de los Clientes extranjeros, no residentes, para que puedan compra viviendas, locales comerciales o realizar inversiones en sociedades y startup en España.
En la actualidad tenemos esta web que puede servir de referencia; www.brixolacapital,com
El diseño final debe comunicar seguridad y responsabilidad en los procesos de inversión.
Necesitamos que la Pagina web sea bilingüe ( Español-Ingles)

```html
<!DOCTYPE html>
<html lang="es">
<head>
<meta charset="utf-8">
<title>BrixolaCapital – Inversión en España</title>
<link href="https://fonts.googleapis.com/css2?family=Mulish:wght@400;600;700;800;900&display=swap" rel="stylesheet">
<style>
:root{
  --navy:#283a7a;
  --navy-2:#33448a;
  --navy-dark:#1f2f6b;
  --ink:#2b2b2b;
  --text:#3a3a3a;
  --white:#ffffff;
  --light:#eef0f3;
}
*{box-sizing:border-box;margin:0;padding:0}
html,body{width:1200px;height:2944px;overflow:hidden}
body{font-family:"Mulish",sans-serif;color:var(--text);background:var(--white);position:relative}
.abs{position:absolute}
.btn{position:absolute;background:var(--navy);color:var(--white);font-weight:800;text-transform:uppercase;display:flex;align-items:center;justify-content:center;letter-spacing:.2px}

/* nav */
.nav{top:0;left:0;width:1200px;height:73px;background:var(--white)}
.brand{position:absolute;border:1px solid #333;font-size:19px;letter-spacing:.6px;color:var(--ink);display:flex;align-items:center;justify-content:center;font-weight:400}
.nav .brand{left:133px;top:21px;width:169px;height:29px}
.nav-links{position:absolute;left:333px;top:26px;display:flex;gap:23px;font-size:13.5px;color:#333}
.nav-links .active{color:var(--navy);font-weight:800;text-decoration:underline;text-underline-offset:3px}
.nav-mail{position:absolute;left:828px;top:26px;font-size:13.5px;color:#333;display:flex;gap:10px;align-items:center}

/* hero */
.hero{top:73px;left:0;width:1200px;height:602px;clip-path:polygon(0 0,100% 0,100% 85%,0 100%);
  background:linear-gradient(180deg,#7a6aa0 0%,#d98a5a 30%,#f0a24a 45%,#9a6a6a 60%,#5e5240 78%,#3f4a2e 100%)}
.hero-accent{background:var(--navy)}
.hero-kicker{left:597px;top:124px;font-size:16px;font-weight:800;color:#3a3340}
.hero-title{left:596px;top:146px;font-size:39px;font-weight:900;color:#3a3340}
.hero-sub{left:597px;top:201px;font-size:16px;color:#3a3340}
.hero .btn,.hero-btn{left:599px;top:246px;width:171px;height:40px;font-size:13px}
.dots{left:563px;top:588px;display:flex;gap:9px}
.dots span{width:12px;height:12px;border:2px solid #fff;border-radius:50%}

/* about */
.about-bg{top:600px;left:0;width:1200px;height:660px;background:linear-gradient(135deg,#fafafa,#eceef1 50%,#fafafa)}
.photo-tower{left:191px;top:717px;width:354px;height:451px;background:linear-gradient(180deg,#9aa3a2 0%,#7e8886 45%,#6d6f6c 100%)}
.bar{background:var(--navy)}
.about-title{left:648px;top:738px;font-size:21px;font-weight:800;color:var(--ink)}
.rule{height:2px;background:var(--navy)}
.about-text{left:652px;top:819px;width:410px;font-size:14.5px;line-height:21px;color:#333}
.about-btn{left:654px;top:1003px;width:232px;height:42px;font-size:13px}

/* values */
.values{top:1189px;left:0;width:1200px;height:497px;clip-path:polygon(0 63px,100% 0,100% 432px,0 497px);display:flex}
.values .col{width:606px;height:100%;background:var(--navy);position:relative}
.values .col + .col{width:594px;background:var(--navy-2)}
.v-icon{position:absolute;width:86px;height:86px}
.v-title{position:absolute;width:100%;text-align:center;font-size:20px;font-weight:900;color:var(--white)}
.v-text{position:absolute;width:100%;text-align:center;font-size:14.5px;line-height:21px;color:#e8ebf5}

/* blog */
.blog{top:1640px;left:0;width:1200px;height:640px;background:linear-gradient(180deg,#e6e9ec 0%,#ece9e4 50%,#e3e6ea 100%);z-index:-1}
.blog-title{left:0;width:1200px;text-align:center;top:1700px;font-size:21px;font-weight:900;color:var(--ink)}
.card{position:absolute;top:1790px;width:292px;height:412px;background:var(--white);box-shadow:0 2px 10px rgba(0,0,0,.05)}
.card-img{height:191px;width:100%}
.card-date{position:absolute;left:26px;top:218px;border:1px solid #444;font-size:11px;padding:2px 8px;color:#333}
.card-title{position:absolute;left:26px;top:262px;width:250px;font-size:14.5px;font-weight:800;line-height:20px;color:var(--ink)}
.card-text{position:absolute;left:26px;width:250px;font-size:11.5px;line-height:16px;color:#444}
.card .btn{left:29px;width:154px;height:27px;font-size:8.5px}
.arrow{position:absolute;width:30px;height:30px;border-radius:50%;background:var(--navy);top:1976px}

/* subscribe */
.subscribe{top:2260px;left:0;width:1200px;height:480px;background:linear-gradient(180deg,#3b5fb0 0%,#8fa8d2 30%,#d8dde6 48%,#b9926a 65%,#7a5a42 85%,#5b4a3f 100%)}
.sub-title{left:131px;top:2302px;font-size:25px;font-weight:900;color:var(--navy)}
.sub-text{left:132px;top:2348px;width:350px;font-size:14px;line-height:18px;color:#222}
.sub-form{left:533px;top:2349px;width:533px;height:54px;border:2px solid var(--navy);background:rgba(255,255,255,.85)}
.sub-form .ph{position:absolute;left:52px;top:16px;font-size:14px;color:#333}
.sub-form .btn{left:405px;top:6px;width:120px;height:38px;font-size:13px}

/* footer */
.footer{top:2690px;left:0;width:1200px;height:254px;background:var(--navy);clip-path:polygon(0 50px,45% 24px,100% 0,100% 100%,0 100%)}
.footer .brand{left:130px;top:93px;width:188px;height:33px;border-color:#fff;color:#fff}
.f-label{left:583px;top:76px;font-size:13px;color:#e6e9f4}
.f-mail{left:841px;top:70px;font-size:13px;color:#e6e9f4;display:flex;gap:10px;align-items:center}
.f-links{left:583px;top:114px;display:flex;gap:30px;font-size:13px;color:#e6e9f4}
.f-rule{left:132px;top:163px;width:936px;height:1px;background:#4d5e9a}
.copy{left:0;width:1200px;text-align:center;top:200px;font-size:11px;color:#e6e9f4}
</style>
</head>
<body>

<header class="abs nav">
  <div class="brand">BrixolaCapital</div>
  <nav class="nav-links">
    <span class="active">Inicio</span><span>Como trabajamos</span><span>Inversiones exitosas</span><span>Contacto</span><span>Actualidad</span>
  </nav>
  <div class="nav-mail">
    <svg width="20" height="15" viewBox="0 0 20 15"><rect x="1" y="1" width="18" height="13" fill="none" stroke="#333" stroke-width="1.4"/><path d="M1 1l9 7 9-7" fill="none" stroke="#333" stroke-width="1.4"/></svg>
    consultas@brixolacapital.com
  </div>
</header>

<section class="abs hero" role="img" aria-label="Vista de Barcelona al atardecer con una basílica en la colina"></section>
<div class="abs hero-accent" style="left:119px;top:655px;width:122px;height:30px;transform:skewY(-3deg)"></div>
<div class="abs hero-accent" style="left:965px;top:574px;width:122px;height:14px;transform:skewY(-3deg)"></div>
<div class="abs hero-kicker">BIENVENIDO</div>
<h1 class="abs hero-title">Inversión en España</h1>
<div class="abs hero-sub">Una Idea Inteligente</div>
<div class="btn hero-btn">Ponte en contacto</div>
<div class="abs dots"><span></span><span></span><span></span><span></span></div>

<section class="abs about-bg" style="z-index:-1"></section>
<div class="abs bar" style="left:181px;top:814px;width:10px;height:335px"></div>
<div class="abs bar" style="left:545px;top:737px;width:12px;height:338px"></div>
<div class="abs photo-tower" role="img" aria-label="Edificio histórico con torre de reloj bajo un cielo nublado"></div>
<h2 class="abs about-title">¿Quiénes somos?</h2>
<div class="abs rule" style="left:652px;top:783px;width:55px"></div>
<p class="abs about-text">Somos un gran equipo de profesionales y empresas asociadas, en España y Latinoamérica, con la misión de respaldarte en tu proyecto "Inversión en España" . Coordinamos, supervisamos y gestionamos todo el proceso de inversión para que los extranjeros no residentes puedan compra viviendas, locales comerciales o realizar inversiones en sociedades y startup en España</p>
<div class="btn about-btn">Consulte mais informação</div>

<section class="abs values">
  <div class="col">
    <svg class="v-icon" style="left:288px;top:100px" viewBox="0 0 86 86"><circle cx="43" cy="43" r="41" fill="none" stroke="#fff" stroke-width="3"/><rect x="35" y="22" width="20" height="28" rx="2" fill="#fff"/><rect x="28" y="30" width="22" height="32" rx="2" fill="#fff" stroke="#283a7a" stroke-width="2"/><path d="M33 40h12M33 46h12M33 52h12" stroke="#283a7a" stroke-width="2.5"/></svg>
    <div class="v-title" style="top:222px;left:21px">Nuestra Filosofía</div>
    <p class="v-text" style="top:265px;left:21px;padding:0 175px">Ayudarte a que puedas invertir en España de una manera segura y rentable, cumpliendo con todos los proceso de inversión en España y acceder a la visa de residencia por inversión.</p>
  </div>
  <div class="col">
    <svg class="v-icon" style="left:195px;top:95px" viewBox="0 0 86 86"><circle cx="43" cy="43" r="41" fill="none" stroke="#fff" stroke-width="3"/><circle cx="41" cy="45" r="22" fill="none" stroke="#fff" stroke-width="4"/><circle cx="41" cy="45" r="13" fill="none" stroke="#fff" stroke-width="4"/><circle cx="41" cy="45" r="4" fill="#fff"/><path d="M41 45l20-20M55 22l8 0 0 8" stroke="#fff" stroke-width="4" fill="none"/></svg>
    <div class="v-title" style="top:222px">Nuestros Objetivos</div>
    <p class="v-text" style="top:265px;padding:0 145px">Encontrarte las mejores y mas rentables oportunidades de inversión en España.</p>
    <p class="v-text" style="top:328px;padding:0 145px">Respaldarte durante todo el proceso con transparencia, honestidad y buscando siempre tu mayor rentabilidad.</p>
  </div>
</section>

<section class="abs blog" role="img" aria-label="Fondo tenue de una plaza monumental de Madrid"></section>
<h2 class="abs blog-title">Mi Blog</h2>
<div class="abs rule" style="left:564px;top:1739px;width:72px"></div>

<div class="arrow" style="left:68px"><svg width="30" height="30" viewBox="0 0 30 30"><path d="M21 15H9M14 10l-5 5 5 5" stroke="#fff" stroke-width="2.4" fill="none"/></svg></div>
<div class="arrow" style="left:1099px"><svg width="30" height="30" viewBox="0 0 30 30"><path d="M9 15h12M16 10l5 5-5 5" stroke="#fff" stroke-width="2.4" fill="none"/></svg></div>

<article class="card" style="left:133px">
  <div class="card-img" role="img" aria-label="Interior de un palacio de cristal con vegetación otoñal" style="background:linear-gradient(180deg,#a7a49a,#c77a4a 60%,#8a4f35)"></div>
  <div class="card-date">4 de febrero de 2021</div>
  <h3 class="card-title">Los proyectos que transformaran Madrid.</h3>
  <p class="card-text" style="top:312px">arte en tu proyecto "Inversión en España" . Coordinamos, supervi</p>
  <div class="btn" style="top:355px">Consulte mais informação</div>
</article>
<article class="card" style="left:455px">
  <div class="card-img" role="img" aria-label="Persona trabajando con un portátil en una cafetería" style="background:linear-gradient(135deg,#8b6a4a,#c9a07a 50%,#6a5040)"></div>
  <div class="card-date">4 de febrero de 2021</div>
  <h3 class="card-title">Particulares acceden a FACTORING</h3>
  <p class="card-text" style="top:312px">Créditos hipotecarios, Estudios Mercado Inmobiliario, Inversiones en Empresas,</p>
  <div class="btn" style="top:355px">Consulte mais informação</div>
</article>
<article class="card" style="left:776px">
  <div class="card-img" role="img" aria-label="Primer plano digital de un ojo con elementos tecnológicos" style="background:linear-gradient(135deg,#5a6a72,#9fc0cc 55%,#d6e6ec)"></div>
  <div class="card-date">4 de febrero de 2021</div>
  <h3 class="card-title">VELTARO Financiación exitosa</h3>
  <p class="card-text" style="top:290px">arte en tu proyecto "Inversión en España" . Coordinamos, supervi</p>
  <div class="btn" style="top:355px">Consulte mais informação</div>
</article>

<section class="abs subscribe" role="img" aria-label="Panorámica de Madrid con cielo azul"></section>
<h2 class="abs sub-title">Suscribete</h2>
<p class="abs sub-text">Al suscribirte recibirás noticias sobre alternativas de proyectos de "Inversión en España", información sobre la visa de residencia y estudios sobre ofertas de bienes raíces</p>
<div class="abs sub-form">
  <svg class="abs" style="left:19px;top:18px" width="20" height="15" viewBox="0 0 20 15"><rect x="1" y="1" width="18" height="13" fill="none" stroke="#283a7a" stroke-width="1.4"/><path d="M1 1l9 7 9-7" fill="none" stroke="#283a7a" stroke-width="1.4"/></svg>
  <span class="ph">Email Id</span>
  <div class="btn">Registrarse</div>
</div>

<footer class="abs footer">
  <div class="brand">BrixolaCapital</div>
  <div class="abs f-label">Inversiones Exitosas</div>
  <div class="abs f-mail">
    <svg width="20" height="15" viewBox="0 0 20 15"><rect x="1" y="1" width="18" height="13" fill="none" stroke="#fff" stroke-width="1.4"/><path d="M1 1l9 7 9-7" fill="none" stroke="#fff" stroke-width="1.4"/></svg>
    consultas@brixolacapital.com
  </div>
  <nav class="abs f-links"><span>Inicio</span><span>Como trabajamos</span><span>Inversiones exitosas</span><span>Contacto</span><span>Actualidad</span></nav>
  <div class="abs f-rule"></div>
  <div class="abs copy">COPYRIGHT © 2022 BRIXOLACAPITAL - TODOS LOS DERECHOS RESERVADOS.</div>
</footer>

</body>
</html>
```